The name of my company is Tolmen Refacing LLC and I would like the sub text to say "Cabinet Refacing and Countertops". Have my name Dorian Tolmen, Owner / Sales, contact info: Cell: 360-555-0147 / Email: dorian.tolmen@quenmail.com

Simple, Clean, and Organized. With colors that will appeal to the eye.

Target Market(s)

Houses and Apartments

Industry/Entity Type

Cabinet Refacing

Contact Information for Business Card

Company name and sub text Dorian Tolmen - Owner / Sales, my cell phone number and email

Requirements
Must have
• Business name, my name / position, and my contact info
Nice to have
• Simple. Organized. Appealing to the eye

```html
<!DOCTYPE html>
<html lang="en">
<head>
<meta charset="utf-8">
<title>Tolmen Refacing LLC – Business Card</title>
<link rel="stylesheet" href="https://fonts.googleapis.com/css2?family=Questrial&family=Lexend:wght@400&display=swap">
<style>
  :root {
    --backdrop: #2b2d30;
    --card-white: #fbfbfb;
    --card-white-end: #eeeeee;
    --navy: #0b1424;
    --navy-deep: #070d18;
    --accent-blue: #3863b4;
    --ink: #1b1f2a;
    --paper-text: #ffffff;
  }
  * { margin: 0; padding: 0; box-sizing: border-box; }
  html, body {
    width: 1200px; height: 732px; overflow: hidden;
    background: var(--backdrop);
  }
  .canvas { position: relative; width: 1200px; height: 732px; }

  .card {
    position: absolute; top: 242px;
    width: 436px; height: 249px;
    box-shadow: 0 6px 18px rgba(0,0,0,0.45);
  }

  /* Front: personal details */
  .card--front {
    left: 144px;
    background: linear-gradient(160deg, var(--card-white) 40%, var(--card-white-end) 100%);
    font-family: "Questrial", sans-serif;
  }
  .edge-bar {
    position: absolute; left: 57px; width: 318px; height: 2px;
    background: var(--navy);
  }
  .edge-bar--top { top: 0; }
  .edge-bar--bottom { bottom: 2px; }

  .identity {
    position: absolute; right: 235px; top: 109px;
    text-align: right; white-space: nowrap;
  }
  .identity__name {
    font-size: 17px; letter-spacing: 1.6px;
    color: var(--accent-blue); line-height: 1;
  }
  .identity__role {
    font-size: 12.5px; color: var(--ink);
    margin-top: 3px; line-height: 1;
  }
  .divider {
    position: absolute; left: 216px; top: 111px;
    width: 1px; height: 26px; background: var(--accent-blue);
  }
  .contact {
    position: absolute; left: 228px; top: 109px;
    list-style: none; font-size: 12px; color: var(--ink);
  }
  .contact__item {
    display: flex; align-items: center; gap: 6px;
    height: 15px; white-space: nowrap;
  }
  .contact__icon { width: 11px; height: 11px; fill: var(--accent-blue); flex: none; }

  /* Back: company */
  .card--back {
    left: 621px;
    background: radial-gradient(ellipse at 25% 20%, #0e1a2d 0%, var(--navy) 45%, var(--navy-deep) 100%);
    text-align: center; color: var(--paper-text);
  }
  .brand-mark {
    position: absolute; left: 50%; top: 74px;
    width: 22px; height: 22px; margin-left: -11px;
    background: var(--accent-blue);
  }
  .brand-name {
    position: absolute; left: 0; right: 0; top: 136px;
    font-family: "Questrial", sans-serif;
    font-size: 25px; letter-spacing: 0.3px; line-height: 1;
  }
  .brand-tagline {
    position: absolute; left: 0; right: 0; top: 170px;
    font-family: "Lexend", sans-serif;
    font-size: 10.5px; letter-spacing: 0.4px; line-height: 1;
  }
</style>
</head>
<body>
<main class="canvas">

  <section class="card card--front" aria-label="Business card front">
    <span class="edge-bar edge-bar--top"></span>
    <div class="identity">
      <p class="identity__name">DORIAN TOLMEN</p>
      <p class="identity__role">Owner / Sales</p>
    </div>
    <span class="divider"></span>
    <ul class="contact">
      <li class="contact__item">
        <svg class="contact__icon" viewBox="0 0 24 24" aria-hidden="true"><path d="M6.6 10.8a15.1 15.1 0 0 0 6.6 6.6l2.2-2.2a1 1 0 0 1 1-.25 11.4 11.4 0 0 0 3.6.57 1 1 0 0 1 1 1V20a1 1 0 0 1-1 1A17 17 0 0 1 3 4a1 1 0 0 1 1-1h3.5a1 1 0 0 1 1 1c0 1.25.2 2.45.57 3.57a1 1 0 0 1-.25 1z"/></svg>
        <span>360-555-0147</span>
      </li>
      <li class="contact__item">
        <svg class="contact__icon" viewBox="0 0 24 24" aria-hidden="true"><path d="M2 5h20v14H2z" fill="none"/><path d="M2 5h20v14H2V5zm2 2v.5l8 5.5 8-5.5V7H4zm0 2.9V17h16V9.9l-8 5.5-8-5.5z"/></svg>
        <span>dorian.tolmen@quenmail.com</span>
      </li>
    </ul>
    <span class="edge-bar edge-bar--bottom"></span>
  </section>

  <section class="card card--back" aria-label="Business card back">
    <span class="brand-mark"></span>
    <h1 class="brand-name">TOLMEN REFACING, LLC</h1>
    <p class="brand-tagline">Cabinet Refacing and Countertops</p>
  </section>

</main>
</body>
</html>
```